Buch-/E-Book-Cover für Sammlung von positiven Erfahrungen
Zielgruppe
die Zielgruppe sind Väter die ihren Söhne eine Sammlung von Empfehlungen für ein positives Leben schenken sollen. Der Titel des Buches heisst 'Zwischen Ebbe und Glut'
Aufgabenstellung
ich möchte mich hier von den Designern überraschen und inspirieren lassen.

```html
<!DOCTYPE html>
<html lang="de">
<head>
<meta charset="utf-8">
<title>Zwischen Ebbe und Glut – Buchcover</title>
<link rel="stylesheet" href="https://fonts.googleapis.com/css2?family=League+Gothic&display=swap">
<style>
  :root {
    --paper: #ffffff;
    --title-blue: #08588c;
    --photo-light: #eef1f4;
    --photo-shirt: #f4f4f4;
    --photo-denim: #3b5d80;
    --photo-shoe: #6e2a35;
  }
  html, body {
    margin: 0;
    padding: 0;
    width: 858px;
    height: 1200px;
    overflow: hidden;
    background: var(--paper);
  }
  .cover {
    position: relative;
    width: 858px;
    height: 1200px;
    background: var(--paper);
  }
  .cover-photo {
    position: absolute;
    left: 56px;
    top: 262px;
    width: 356px;
    height: 932px;
    border-radius: 40px 40px 8px 8px;
    background: linear-gradient(
      to bottom,
      var(--photo-light) 0%,
      var(--photo-shirt) 45%,
      var(--photo-denim) 62%,
      var(--photo-denim) 92%,
      var(--photo-shoe) 100%
    );
  }
  .cover-title {
    position: absolute;
    left: 0;
    top: 0;
    width: 858px;
    height: 1200px;
  }
  .cover-title text {
    font-family: "League Gothic", "Oswald", sans-serif;
    fill: var(--title-blue);
  }
</style>
</head>
<body>
  <main class="cover">
    <div class="cover-photo" role="img" aria-label="Foto: Vater und Sohn stehen nebeneinander in weißen T-Shirts und Jeans, der Vater legt die Hand auf die Schulter des Sohnes"></div>

    <svg class="cover-title" viewBox="0 0 858 1200" aria-label="Zwischen Ebbe und Glut">
      <text class="title-word title-word--small" x="446" y="262" font-size="165" textLength="394" lengthAdjust="spacingAndGlyphs">Zwischen</text>
      <text class="title-word title-word--large" x="433" y="593" font-size="430" textLength="407" lengthAdjust="spacingAndGlyphs">Ebbe</text>
      <text class="title-word title-word--small" x="646" y="778" font-size="280" textLength="184" lengthAdjust="spacingAndGlyphs">und</text>
      <text class="title-word title-word--large" x="477" y="1110" font-size="430" textLength="349" lengthAdjust="spacingAndGlyphs">Glut</text>
    </svg>
  </main>
</body>
</html>
```